Brinevale Yacht Management Full Page Ad Flyer

Yacht Management Package also includes the following periodic Monthly services:

Monthly full vessel systems checklist inspections
Diver For Hull Cleaning And Inspection Of Props, Shafts, and Zincs
Interior/Exterior Detailing and scheduled washdowns
Manage Haulout
Pump-out Services
On-call Captain and Crew Services
Updates

Need more time to provide more content to designers and the printing press template file.

Target Market(s)

Vessel owners, motor yachts, sailboats from 25 feet in length up to 125 feet in length. We do not do cruise ships or yachts larger than 125 feet. Someone who has their boat docked at their house or a local marina. We also offer mobile on-site services.

```html
<!DOCTYPE html>
<html lang="en">
<head>
<meta charset="utf-8">
<title>Brinevale Yacht Management – Yacht Management Package</title>
<link rel="stylesheet" href="https://fonts.googleapis.com/css2?family=Bebas+Neue&family=Kaushan+Script&family=Montserrat:wght@400;500;600&family=Oswald:wght@200;500&display=swap">
<style>
  :root {
    --blue-deep: #2460ad;
    --blue-mid: #1f6ab4;
    --blue-strip: #1b70ba;
    --blue-light: #7db6e6;
    --blue-ink: #1c58a6;
    --white: #ffffff;
    --page: #e8e9eb;
  }
  * { margin: 0; padding: 0; box-sizing: border-box; }
  html, body { width: 851px; height: 1200px; overflow: hidden; background: var(--page); }
  .flyer {
    position: relative; width: 851px; height: 1200px; overflow: hidden;
    background: var(--blue-strip);
    font-family: "Montserrat", sans-serif; color: var(--white);
  }
  .main-panel {
    position: absolute; left: 0; top: 0; width: 495px; height: 1200px;
    background: linear-gradient(170deg, var(--blue-deep) 0%, var(--blue-mid) 100%);
  }
  .abs { position: absolute; }

  .brand { left: 0; width: 370px; top: 78px; text-align: center; }
  .brand-name { font-family: "Montserrat", sans-serif; font-weight: 500; font-size: 40px; letter-spacing: 3px; line-height: 1; }
  .brand-sub { font-size: 10.5px; letter-spacing: 5.5px; margin-top: 6px; }

  .title-script { left: 20px; top: 176px; font-family: "Kaushan Script", cursive; font-size: 118px; line-height: 1; z-index: 2; }
  .title-block { left: 47px; top: 280px; font-family: "Bebas Neue", sans-serif; font-size: 98px; line-height: 0.73; z-index: 1; }
  .title-block .light { color: var(--blue-light); display: block; }
  .title-block .white { color: var(--white); display: block; margin-top: 8px; }

  .divider { left: 43px; top: 465px; width: 143px; height: 3px; background: var(--white); }

  .headline { left: 43px; top: 485px; font-family: "Bebas Neue", sans-serif; font-size: 38px; line-height: 0.9; }

  .services { left: 0; top: 0; list-style: none; }
  .service { position: absolute; left: 37px; display: flex; align-items: center; width: 460px; }
  .service-num {
    position: relative; flex: none; width: 47px; height: 47px; border: 2.5px solid var(--white); border-radius: 50%;
    display: flex; align-items: center; justify-content: center; font-weight: 600; font-size: 13px;
  }
  .service-num::after {
    content: ""; position: absolute; right: -6px; top: 50%; width: 11px; height: 11px; margin-top: -5.5px;
    background: var(--white); border-radius: 50%;
  }
  .service-text { margin-left: 21px; font-weight: 600; font-size: 18px; line-height: 23px; }

  .range { left: 38px; top: 912px; border-left: 15px solid var(--white); padding-left: 10px; }
  .range-title { font-family: "Bebas Neue", sans-serif; font-size: 38px; line-height: 30px; padding-top: 2px; }
  .range-note { font-size: 15px; line-height: 21px; margin-top: 4px; }

  .badge { left: 322px; top: 905px; width: 152px; height: 152px; }
  .badge-text {
    position: absolute; left: 322px; top: 944px; width: 152px; text-align: center;
    font-family: "Oswald", sans-serif; color: var(--blue-ink); font-size: 25px; line-height: 24px;
  }
  .badge-text .bold { font-weight: 500; display: block; }
  .badge-text .thin { font-weight: 200; display: block; }
  .badge-text .rule { display: block; width: 56px; height: 1.5px; background: var(--blue-ink); margin: 3px auto 0; }

  .call { left: 37px; top: 1108px; font-family: "Bebas Neue", sans-serif; }
  .call-label { font-size: 30px; line-height: 26px; }
  .call-number { font-size: 45px; line-height: 44px; }
  .contact { right: 16px; top: 1138px; text-align: right; font-size: 13px; line-height: 17px; font-style: normal; }

  .photo-frame { position: absolute; left: 495px; width: 345px; background: var(--white); padding: 6px 6px; }
  .photo { width: 100%; height: 100%; }
  .photo-yacht { background: linear-gradient(150deg, #0f3554 0%, #2a5b7a 45%, #d9dfe3 70%, #355f7c 100%); }
  .photo-engine { background: linear-gradient(120deg, #1a1d22 0%, #3a3f47 45%, #c9cfd4 70%, #2b3f6a 100%); }
  .photo-deck { background: linear-gradient(160deg, #8a7a66 0%, #e4e2df 40%, #9aa4aa 75%, #5a6068 100%); }
</style>
</head>
<body>
<main class="flyer">
  <section class="main-panel">
    <header class="brand abs">
      <div class="brand-name">BRINEVALE</div>
      <div class="brand-sub">YACHT MANAGEMENT</div>
    </header>

    <h1>
      <span class="title-script abs">Yacht</span>
      <span class="title-block abs"><span class="light">MANAGEMENT</span><span class="white">PACKAGE</span></span>
    </h1>

    <div class="divider abs"></div>
    <h2 class="headline abs">MONTHLY FULL VESSEL SYSTEMS<br>CHECKLIST INSPECTIONS</h2>

    <ol class="services abs">
      <li class="service" style="top:585px"><span class="service-num">01</span><span class="service-text">Diver For Hull Cleaning &amp; Inspection<br>Of Props, Shafts And Zincs</span></li>
      <li class="service" style="top:640px"><span class="service-num">02</span><span class="service-text">Manage Haulout</span></li>
      <li class="service" style="top:697px"><span class="service-num">03</span><span class="service-text">Interior/exterior Detailing &amp;<br>Scheduled Washdowns</span></li>
      <li class="service" style="top:756px"><span class="service-num">04</span><span class="service-text">Pump-out Services</span></li>
      <li class="service" style="top:813px"><span class="service-num">05</span><span class="service-text">On-call Captain &amp;<br>Crew Services</span></li>
    </ol>

    <div class="range abs">
      <p class="range-title">SAILBOATS FROM 25<br>FEET IN LENGTH UP TO<br>125 FEET IN LENGTH.</p>
      <p class="range-note">Services offered at house<br>or a local marina.</p>
    </div>

    <div class="call abs">
      <div class="call-label">CALL US TODAY</div>
      <div class="call-number">012-555-0198</div>
    </div>
    <address class="contact abs">hello@brinevale.com<br>www.brinevale.com</address>
  </section>

  <svg class="badge abs" viewBox="0 0 152 152" aria-hidden="true">
    <g fill="#7db6e6">
      <circle cx="76" cy="76" r="64"/>
      <circle cx="76" cy="12" r="18"/><circle cx="108" cy="20.6" r="18"/><circle cx="131.4" cy="44" r="18"/>
      <circle cx="140" cy="76" r="18"/><circle cx="131.4" cy="108" r="18"/><circle cx="108" cy="131.4" r="18"/>
      <circle cx="76" cy="140" r="18"/><circle cx="44" cy="131.4" r="18"/><circle cx="20.6" cy="108" r="18"/>
      <circle cx="12" cy="76" r="18"/><circle cx="20.6" cy="44" r="18"/><circle cx="44" cy="20.6" r="18"/>
    </g>
    <g fill="#ffffff">
      <circle cx="76" cy="76" r="60"/>
      <circle cx="76" cy="15" r="14"/><circle cx="106.5" cy="23.2" r="14"/><circle cx="128.8" cy="45.5" r="14"/>
      <circle cx="137" cy="76" r="14"/><circle cx="128.8" cy="106.5" r="14"/><circle cx="106.5" cy="128.8" r="14"/>
      <circle cx="76" cy="137" r="14"/><circle cx="45.5" cy="128.8" r="14"/><circle cx="23.2" cy="106.5" r="14"/>
      <circle cx="15" cy="76" r="14"/><circle cx="23.2" cy="45.5" r="14"/><circle cx="45.5" cy="23.2" r="14"/>
    </g>
  </svg>
  <div class="badge-text">
    <span class="bold">MOBILE</span><span class="thin">ON-SITE</span><span class="bold">SERVICE</span><span class="rule"></span>
  </div>

  <figure class="photo-frame" style="top:-2px;height:298px">
    <div class="photo photo-yacht" role="img" aria-label="Photo of a white motor yacht cruising at speed over dark blue water"></div>
  </figure>
  <figure class="photo-frame" style="top:318px;height:508px">
    <div class="photo photo-engine" role="img" aria-label="Photo of a technician in gloves servicing a black outboard engine"></div>
  </figure>
  <figure class="photo-frame" style="top:848px;height:352px">
    <div class="photo photo-deck" role="img" aria-label="Photo of a crew member scrubbing a yacht deck with a long-handled brush"></div>
  </figure>
</main>
</body>
</html>
```